Business Card Design

We sell fish products to corporate food companies who then turn these products into final food products for consumers

Industry/Entity Type

Business

Contact Information for Business Card

I need a corporate business card template for a fish products business. We would like it be professional for use in dealing with multi national companies. This company business card template will be used by multiple employees so the following fields must be open to edit (Name, Phone Number and Email address)

```html
<!DOCTYPE html>
<html lang="en">
<head>
<meta charset="UTF-8">
<title>Coral Bay Seafoods – Business Card</title>
<link rel="stylesheet" href="https://fonts.googleapis.com/css2?family=Mulish:wght@400;700&display=swap">
<style>
  :root {
    --page-bg: #e9ebee;
    --card-white: #fbfcfd;
    --navy: #123f8c;
    --ocean: #1c6fc0;
    --ocean-deep: #0f4f9e;
    --ocean-light: #3d8fd6;
    --sea-green: #3f9e5e;
    --text-light: #e4eef8;
  }
  * { margin: 0; padding: 0; box-sizing: border-box; }
  html, body {
    width: 1200px;
    height: 970px;
    overflow: hidden;
    background: var(--page-bg);
    font-family: "Mulish", sans-serif;
  }
  .business-card {
    position: absolute;
    left: 100px;
    top: 205px;
    width: 1000px;
    height: 560px;
    border-radius: 26px;
    background: var(--card-white);
    overflow: hidden;
    box-shadow: 0 10px 30px rgba(20, 40, 70, 0.18);
  }
  .wave-band {
    position: absolute;
    inset: 0;
    width: 100%;
    height: 100%;
  }
  .brand {
    position: absolute;
    left: 480px;
    top: 70px;
    width: 490px;
    text-align: center;
  }
  .brand-dot {
    display: block;
    width: 96px;
    height: 96px;
    margin: 0 auto 18px;
    border-radius: 50%;
    background: var(--ocean-deep);
  }
  .brand-name {
    font-size: 50px;
    font-weight: 700;
    line-height: 1.08;
    letter-spacing: 1px;
    color: var(--navy);
    text-transform: uppercase;
  }
  .contact {
    position: absolute;
    left: 50px;
    top: 396px;
    color: var(--text-light);
    font-size: 22px;
    line-height: 28px;
  }
  .contact-address { margin-bottom: 16px; }
  .contact-line {
    display: flex;
    align-items: center;
    gap: 8px;
  }
  .contact-line svg { width: 16px; height: 16px; flex: none; }
  .holder {
    position: absolute;
    right: 48px;
    top: 490px;
    color: var(--text-light);
    font-size: 24px;
  }
  .holder-name { font-weight: 700; }
  .holder-role { font-weight: 400; }
</style>
</head>
<body>
  <div class="business-card">
    <svg class="wave-band" viewBox="0 0 1000 560" preserveAspectRatio="none" aria-hidden="true">
      <defs>
        <linearGradient id="oceanFill" x1="0" y1="0" x2="0" y2="1">
          <stop offset="0" stop-color="var(--ocean-light)"/>
          <stop offset="1" stop-color="var(--ocean-deep)"/>
        </linearGradient>
      </defs>
      <path d="M0 330 C90 285 150 262 230 264 C380 268 560 392 740 389 C860 387 940 364 1000 352 L1000 560 L0 560 Z" fill="var(--sea-green)"/>
      <path d="M0 340 C90 295 150 274 230 276 C380 280 560 404 740 401 C860 399 940 376 1000 364 L1000 560 L0 560 Z" fill="var(--card-white)"/>
      <path d="M0 348 C90 304 150 284 230 286 C380 290 560 414 740 411 C860 409 940 386 1000 374 L1000 560 L0 560 Z" fill="var(--navy)"/>
      <path d="M0 362 C90 320 150 302 230 304 C380 310 560 440 740 437 C860 435 940 405 1000 390 L1000 560 L0 560 Z" fill="url(#oceanFill)"/>
    </svg>

    <div class="brand">
      <span class="brand-dot"></span>
      <div class="brand-name">Coral Bay<br>Seafoods</div>
    </div>

    <div class="contact">
      <p class="contact-address">14 Harbour Lane<br>Portside VIC 3999</p>
      <p class="contact-line">
        <svg viewBox="0 0 16 16" aria-hidden="true"><path d="M3.5 1.5l2.5 3-1.5 1.8c.9 1.9 2.3 3.3 4.2 4.2L10.5 9l3 2.5-1.6 2.6C6.8 13.6 2.4 9.2 1 4.1z" fill="currentColor"/></svg>
        + 000 123 4567
      </p>
      <p class="contact-line">
        <svg viewBox="0 0 16 16" aria-hidden="true"><rect x="1" y="3.5" width="14" height="9" fill="currentColor"/><path d="M1.5 4l6.5 5 6.5-5" stroke="var(--ocean)" stroke-width="1.4" fill="none"/></svg>
        info@coralbayseafoods.com
      </p>
    </div>

    <p class="holder"><span class="holder-name">Daniel Reeve</span> <span class="holder-role">/Manager</span></p>
  </div>
</body>
</html>
```